Harbor Crest Data Systems Needs a Website Desing

We need a website design for a new company based in Kuwait called Harbor Crest Data Systems (HCDS). We provide Software as a Service (SaaS) solutions for small and medium business companies. We will develop the required E-systems like HR,Payroll,Accounting Systems for those customers who wants to focus on their business instead of wasting time to automate it. HCDS need a web site that represent this activity and showing our cloud products and allow out customers to easily identify their needs. as a normal web site basic things need to be included like :
about HCDS
Solutions
PressRoom
Contact us
please i need something similar to trelvoxa.com or qup.com or www.dro7lak.com with blue and black theme .. please check the Company's logo
Updates
hi all ,,,
the project is only design without any codes
Reason: The project is focus on design only ,, i will be really appreciated to have more designs

```html
<!DOCTYPE html>
<html lang="en">
<head>
<meta charset="utf-8">
<title>HCDS – Cloud computing made easy</title>
<link href="https://fonts.googleapis.com/css2?family=Exo+2:wght@300;400;500&family=Open+Sans:ital,wght@0,400;0,600;0,700;1,400&display=swap" rel="stylesheet">
<style>
:root{
  --blue:#1a9ad6;
  --blue-dark:#0f7bb0;
  --ink:#111;
  --text:#444;
  --muted:#777;
  --page:#fff;
  --band:#ececec;
  --footer:#e6e6e6;
  --footer-bar:#555;
  --nav-top:#3c3c3c;
  --nav-bottom:#1c1c1c;
  --btn-grey:#d4d4d4;
}
*{margin:0;padding:0;box-sizing:border-box}
html,body{width:887px;height:1200px;overflow:hidden}
body{position:relative;background:var(--page);font-family:"Open Sans",sans-serif;color:var(--text)}
.abs{position:absolute}

.band{left:0;top:413px;width:887px;height:110px;background:linear-gradient(var(--band),var(--page))}

/* header */
.brand{left:35px;top:32px;font-family:"Open Sans",sans-serif;font-weight:600;font-size:24px;color:#2a2a2a;line-height:30px}
.account{right:35px;top:36px;font-size:13px;color:var(--blue)}
.account span{color:#bbb;margin:0 6px}

/* hero */
.hero{left:35px;top:97px;width:817px;height:382px;background:#fff;border:1px solid #d6d6d6;box-shadow:0 14px 24px -14px rgba(0,0,0,.25)}
.nav{height:43px;background:linear-gradient(var(--nav-top),var(--nav-bottom));display:flex}
.nav a{color:#fff;text-decoration:none;font-size:15px;line-height:43px;padding:0 19px}
.nav a.active{background:var(--blue);padding:0 19px}
.hero-title{left:52px;top:58px;font-family:"Exo 2",sans-serif;font-weight:300;font-size:31px;color:var(--ink)}
.hero-sub{left:52px;top:98px;font-family:"Exo 2",sans-serif;font-weight:400;font-size:18px;color:var(--ink)}
.hero-text{left:52px;top:133px;width:302px;font-size:12.4px;line-height:20.5px;color:var(--text)}
.btn-primary{left:52px;top:276px;width:114px;height:30px;background:var(--blue);color:#fff;font-size:12px;font-weight:600;text-align:center;line-height:30px}
.hero-media{left:397px;top:62px;width:366px;height:244px;background:#fff;border:1px solid #ddd;padding:4px;box-shadow:0 1px 4px rgba(0,0,0,.2)}
.hero-media div{width:100%;height:100%;background:radial-gradient(ellipse at 55% 35%,#1c5a78 0%,#0b2333 45%,#03080d 100%)}
.dots{left:382px;top:339px;display:flex;gap:12px}
.dots i{width:9px;height:9px;background:#555;display:block}
.dots i.on{background:var(--blue)}

/* content columns */
.col-title{font-size:17px;color:var(--blue);text-transform:uppercase;font-weight:400;letter-spacing:.3px}
.lead{font-size:11px;font-weight:700;color:var(--ink);line-height:14px;text-align:justify}
.body-text{font-size:11px;line-height:13.5px;color:var(--muted);text-align:justify}
.btn-more{width:99px;height:23px;background:var(--btn-grey);font-size:11.5px;color:#555;text-align:center;line-height:23px;text-transform:uppercase}
.col-1{left:35px;top:545px;width:261px}
.col-2{left:345px;top:545px;width:273px}
.col-3{left:665px;top:545px;width:187px}
.col-1 .lead,.col-2 .lead{margin-top:16px}
.col-1 .body-text{margin-top:16px}
.col-1 .body-text + .body-text{margin-top:11px}
.col-2 .body-text{margin-top:11px}
.chart{left:353px;top:667px;width:250px;height:147px;background:linear-gradient(0deg,#eef3f6,#2a8fc4 30%,#e9f3f9)}
.quote{margin-top:16px;text-align:right;font-size:10.6px;line-height:14px;color:var(--muted)}
.quote b{display:block;color:#555;font-weight:700}
.quote + .quote{margin-top:42px}

/* footer */
.footer{left:0;top:900px;width:887px;height:255px;background:var(--footer)}
.f-title{font-size:12.5px;color:#555;font-weight:600}
.f-address{left:35px;top:942px;font-size:10px;line-height:13px;color:#777}
.f-map{left:35px;top:987px;width:262px;height:133px;background:radial-gradient(ellipse,#c2c2c2 30%,#e0e0e0 75%)}
.links{list-style:none;margin-top:14px}
.links li{font-size:10.5px;color:#777;line-height:25.3px}
.links li::before{content:"› "}
.follow{right:35px;top:908px;display:flex;align-items:center;gap:6px}
.follow span{font-size:13px;color:#444;margin-right:2px;letter-spacing:.3px}
.follow i{width:28px;height:28px;background:var(--blue-dark);display:block}
.bottom{left:0;top:1155px;width:887px;height:45px;background:var(--footer-bar);color:#fff;font-size:11px}
.bottom p{position:absolute;top:15px}
</style>
</head>
<body>
<div class="abs band"></div>

<header>
  <div class="abs brand">Harbor Crest Data Systems</div>
  <div class="abs account">Login<span>|</span>Support</div>
</header>

<section class="abs hero">
  <nav class="nav">
    <a class="active">Home</a><a>Solutions</a><a>PressRoom</a><a>About HCDS</a><a>Contact</a>
  </nav>
  <h1 class="abs hero-title">Welcome to HCDS</h1>
  <h2 class="abs hero-sub">Cloud computing made easy</h2>
  <p class="abs hero-text">Lorem ipsum dolor sit amet, consectetur adipiscing elit. Mauris ante nisl, semper in viverra id, sodales sit amet nulla. Pellentesque sapien libero, viverra sit amet scelerisque sit amet, fermentum quis risus. Maecenas sit amet ipsum a urna viverra vestibulum laoreet vitae nibh.</p>
  <div class="abs btn-primary">Read more</div>
  <div class="abs hero-media"><div role="img" aria-label="Photo of server rack cabling lit by blue lights"></div></div>
  <div class="abs dots"><i class="on"></i><i></i><i></i></div>
</section>

<section class="abs col-1">
  <h3 class="col-title">What we can do for you</h3>
  <p class="lead">Lorem ipsum dolor sit amet, consectetur adipiscing elit.</p>
  <p class="body-text">Mauris ante nisl, semper in viverra id, sodales sit amet nulla. Pellentesque sapien libero, viverra sit amet scelerisque sit amet, fermentum quis risus.</p>
  <p class="body-text">Maecenas sit amet ipsum a urna viverra vestibulum laoreet vitae nibh. Praesent ullamcorper, turpis condimentum dictum volutpat, nunc nunc tempus leo, et porta lacus tortor non nisl. Mauris blandit cursus aliquam.</p>
  <p class="body-text">Suspendisse elementum euismod turpis nec pellentesque. Aliquam eu luctus nisi. Nullam volutpat venenatis nulla, ut tristique lectus mattis quis. Sed massa eros, hendrerit ullamcorper porta et, scelerisque tristique ligula.</p>
</section>
<div class="abs btn-more" style="left:197px;top:844px">Read more</div>

<section class="abs col-2">
  <h3 class="col-title">Time is money</h3>
  <p class="lead">Phasellus metus sem, condimentum id congue eget, ultrices facilisis dolor.</p>
  <p class="body-text">Duis sagittis semper mattis. Cras semper dignissim leo id lobortis. Sed ut mollis nisi. Nam quis neque eu risus interdum vestibulum.</p>
</section>
<div class="abs chart" role="img" aria-label="Illustration of rising blue bar steps with two figures carrying puzzle pieces"></div>
<div class="abs btn-more" style="left:519px;top:844px">Read more</div>

<section class="abs col-3">
  <h3 class="col-title">Testimonials</h3>
  <p class="quote">«In vitae tellus in erat luctus consectetur et non ligula»<b>Happy customer #1</b></p>
  <p class="quote">«Sed tempus feugiat sagittis. Vivamus vel pulvinar purus. Pellentesque quis leo turpis, in hendrerit libero !»<b>Another happy customer</b></p>
  <p class="quote">«Proin interdum elit id felis consectetur pulvinar.»<b>Yet another happy one</b></p>
</section>
<div class="abs btn-more" style="left:754px;top:844px">Read more</div>

<footer>
  <div class="abs footer"></div>
  <h4 class="abs f-title" style="left:35px;top:914px">HCDS - Harbor Crest Data Systems</h4>
  <p class="abs f-address">41 Relay Lane,<br>Kuwait City 70412, Kuwait</p>
  <div class="abs f-map" role="img" aria-label="World map marking the Kuwait office"></div>

  <div class="abs" style="left:345px;top:914px">
    <h4 class="f-title">Useful links</h4>
    <ul class="links">
      <li>Try our services for free</li><li>Our prices</li><li>Frequently Asked Questions</li><li>Work with us</li><li>Affiliate program</li><li>Write about us</li><li>About us</li>
    </ul>
  </div>
  <div class="abs" style="left:534px;top:914px">
    <h4 class="f-title">Get support</h4>
    <ul class="links"><li>Subscribe</li><li>Get in touch</li><li>Troubleshooting</li></ul>
  </div>
  <div class="abs follow"><span>FOLLOW US</span><i aria-label="Social network 1"></i><i aria-label="Social network 2"></i><i aria-label="Social network 3"></i></div>

  <div class="abs bottom">
    <p style="left:35px">Copyright © 2013 HCDS - All rights reserved</p>
    <p style="right:35px">Terms of service</p>
  </div>
</footer>
</body>
</html>
```